Holiday Rental Company Flyer Design (DL not A5)

Note from PixelFolk Administration: The category sizing selected is A5, however the project requires DL sized artwork. Please refer to the DL template link below while the 'Special Requirements' are updated accordingly.

Project Brief:
We need a double sided DL flyer designed for an up market Holiday Rental Company that portrays a personalised approach to property management. These are to be used for letter box drops to homes we're specifically targeting so the design should be modern, complimentary colour palette, uncluttered & visually appealing.

Please Download the DL Template from Quillmark here: http://www.quillmark.com.au/qm/ns/propath/UploadResources.aspx?selectedTab=0?pfid=BFB&pf_id=BFB&xnav=easypath-upload-image#Templates

Target Market(s)

Wealthy Home Owners

Industry/Entity Type

It Company

Font styles to use
Other font styles liked:
• Avant Garde Extra Light & Demi

Colors
33b8a4

Requirements
Must have
• DL Flyer sizes (210mm width x 99mm width, plus 3mm bleed)
• Front: Logo, Main Image & Grab
• Back: Contact Details & Brief Description of our business
• Images: Ideally the main image should be the house with the pool but alternatively a lifestyle images could also be used.
Nice to have
• A creative designer!
Should not have
• Clutter & busy designs

```html
<!DOCTYPE html>
<html lang="en">
<head>
<meta charset="utf-8">
<title>Harbourline Stays – DL Flyer</title>
<link href="https://fonts.googleapis.com/css2?family=Poppins:wght@300;400&display=swap" rel="stylesheet">
<style>
  :root {
    --backdrop: #e4e4e4;
    --teal: #1cb092;
    --teal-brand: #2fae9a;
    --teal-soft: #a9ddd2;
    --teal-heading: #b5ebe0;
    --paper: #f6f8f8;
    --white: #ffffff;
    --ink-grey: #8a8a8a;
  }
  * { box-sizing: border-box; margin: 0; padding: 0; }
  html, body { width: 1200px; height: 900px; overflow: hidden; }
  body {
    background: var(--backdrop);
    font-family: "Poppins", sans-serif;
    position: relative;
  }
  .flyer {
    position: absolute;
    top: 33px;
    width: 404px;
    height: 827px;
    overflow: hidden;
  }
  .flyer--front { left: 162px; background: var(--teal); }
  .flyer--back { left: 645px; background: var(--white); }

  /* Front */
  .front-top {
    position: absolute; left: 0; top: 0; width: 100%; height: 290px;
    background: var(--paper);
  }
  .brand {
    position: absolute; top: 118px; left: 0; width: 100%;
    text-align: center; color: var(--teal-brand);
    font-weight: 400; font-size: 28px; line-height: 36px; letter-spacing: 0;
  }
  .hero-photo {
    position: absolute; left: 0; top: 285px; width: 100%; height: 350px;
    background: linear-gradient(160deg, #1a1c3a 0%, #2c2850 30%, #8a6a3a 52%, #d8b878 62%, #2a6fc4 80%, #4aa6e8 100%);
  }
  .wave { position: absolute; left: 0; width: 100%; display: block; }
  .wave--top { top: 268px; }
  .wave--bottom { top: 612px; }
  .tagline {
    position: absolute; top: 688px; left: 0; width: 100%;
    text-align: center; color: var(--white);
    font-weight: 400; font-size: 19px; line-height: 26px;
  }

  /* Back */
  .band-teal { position: absolute; left: 0; width: 100%; background: var(--teal); color: var(--white); }
  .band-intro { top: 0; height: 174px; padding: 60px 26px 0; }
  .band-service { top: 336px; height: 148px; padding: 24px 26px 0; }
  .section-heading {
    color: var(--teal-heading); font-weight: 400; font-size: 16px; margin-bottom: 18px;
  }
  .body-copy {
    font-weight: 300; font-size: 11.5px; line-height: 16px; text-align: justify;
  }
  .body-copy + .body-copy { margin-top: 16px; }
  .photo-row {
    position: absolute; left: 0; width: 100%; display: flex; gap: 2px;
    background: var(--teal-soft);
  }
  .photo-row--rooms { top: 174px; height: 162px; }
  .photo-row--sea { top: 484px; height: 164px; }
  .photo { height: 100%; }
  .photo--bedroom { width: 200px; background: linear-gradient(150deg, #d8c7a8 0%, #c9b27a 40%, #d8cf48 60%, #b88a6a 100%); }
  .photo--vase { flex: 1; background: linear-gradient(160deg, #9a9a98 0%, #7b7670 45%, #c07a3a 75%, #e2d2c0 100%); }
  .photo--dolphins { width: 208px; background: linear-gradient(170deg, #3cc6c8 0%, #2bb7b8 50%, #7dd8d4 100%); }
  .photo--boat { flex: 1; background: linear-gradient(180deg, #c9d2d6 0%, #aebdc4 45%, #6f9aa6 70%, #8fb4b8 100%); }
  .contact {
    position: absolute; top: 648px; left: 0; width: 100%; padding: 20px 26px 0;
    color: var(--ink-grey); font-weight: 300; font-size: 11.5px; line-height: 16px;
  }
  .contact-list { list-style: none; margin-top: 16px; }
</style>
</head>
<body>
  <section class="flyer flyer--front">
    <div class="front-top">
      <h1 class="brand">Harbourline Stays</h1>
    </div>
    <div class="hero-photo" role="img" aria-label="Modern holiday home at dusk with a lit glass-fenced swimming pool"></div>
    <svg class="wave wave--top" width="404" height="30" viewBox="0 0 404 30" preserveAspectRatio="none">
      <path d="M0 0 Q202 22 404 0 L404 20 Q202 30 0 20 Z" fill="#a9ddd2"/>
    </svg>
    <svg class="wave wave--bottom" width="404" height="30" viewBox="0 0 404 30" preserveAspectRatio="none">
      <path d="M0 6 Q202 -6 404 6 L404 30 L0 30 Z" fill="#a9ddd2"/>
      <path d="M0 18 Q202 4 404 18 L404 30 L0 30 Z" fill="#1cb092"/>
    </svg>
    <p class="tagline">Holiday Rental Management<br>with A Difference</p>
  </section>

  <section class="flyer flyer--back">
    <div class="band-teal band-intro">
      <h2 class="section-heading">What we do differently!</h2>
      <p class="body-copy">Rather than relying upon a key safe or a central pick-up destination, a 'Harbourline Stays' staff member will greet guests upon arrival.</p>
    </div>
    <div class="photo-row photo-row--rooms">
      <div class="photo photo--bedroom" role="img" aria-label="Bed with yellow cushions and a colourful geometric quilt"></div>
      <div class="photo photo--vase" role="img" aria-label="Glass vase of orange flowers with candles on a table"></div>
    </div>
    <div class="band-teal band-service">
      <p class="body-copy">Our 'Meet &amp; Greet' service provides home owners with an increased level of Security and also allows us to:</p>
      <p class="body-copy">Prepare the home for their arrival (lights, heaters, music etc).<br>Establish a rapport &amp; help facilitate future bookings.<br>Reiterate their responsibilities to ensure the return of their bond.</p>
    </div>
    <div class="photo-row photo-row--sea">
      <div class="photo photo--dolphins" role="img" aria-label="Dolphins swimming in clear turquoise water"></div>
      <div class="photo photo--boat" role="img" aria-label="Small sailing boat moored on a calm bay"></div>
    </div>
    <div class="contact">
      <p>If you'd like to know what your property could achieve or require additional information, please contact us on:</p>
      <ul class="contact-list">
        <li>t &nbsp;: (03)5900 4127</li>
        <li>e : stay@harbourlinestays.com.au</li>
        <li>w : harbourlinestays.com.au</li>
        <li>PO Box 48, Tidewater Victoria 3950</li>
      </ul>
    </div>
  </section>
</body>
</html>
```